Brightacre - online store for farm produce

Online store selling fresh produce (vegetables, fruits, dairy products, meat, ...) from various farmers. Every farm has its own shopping window - order page - just like a really simple web store.

Please check the attached design brief and mock-ups for further details.

Target Market(s)

People looking for fresh vegetables, fruit, meat, ... delivered from farms

Industry/Entity Type

Farming

Coding

Coded - Design and coding required

Number of Pages Required

5+ page

Font styles to use
Sans Serif

Requirements
Must have
• Custom design. Good UX/UI design, very functional.
Responsive using bootstrap 12 point grid system

```html
<!DOCTYPE html>
<html lang="en">
<head>
<meta charset="utf-8">
<title>Brightacre – Direct From Farm</title>
<link href="https://fonts.googleapis.com/css2?family=Poppins:wght@300;400;500;600;700&display=swap" rel="stylesheet">
<style>
:root{
  --green:#7cbb10;
  --ink:#222;
  --text:#333;
  --muted:#666;
  --soft:#f4f5f7;
  --dark:#2e2f3e;
  --black:#14141a;
  --white:#fff;
}
*{margin:0;padding:0;box-sizing:border-box}
html,body{width:1200px;height:3016px;overflow:hidden}
body{font-family:'Poppins',sans-serif;color:var(--text);background:var(--white);position:relative}
.abs{position:absolute}
a{color:inherit;text-decoration:none}

.topbar{left:0;top:0;width:1200px;height:44px;border-bottom:1px solid #e6e6e6;font-size:14px;color:#333}
.topbar .welcome{left:44px;top:13px}
.topbar .links{right:44px;top:12px}
.header{left:0;top:44px;width:1200px;height:80px}
.header .contact{top:24px;font-size:12px;font-style:italic;color:#555;display:flex;align-items:center;gap:8px}
.logo{left:0;width:1200px;top:14px;text-align:center;font-size:40px;font-weight:700;letter-spacing:1px;color:var(--ink)}
.header .tool{top:24px;font-size:12px;font-style:italic;color:#666;display:flex;align-items:center;gap:8px}
.nav{left:0;top:124px;width:1200px;height:35px;background:var(--green);color:#fff;font-size:15px;font-weight:600}
.nav span{position:absolute;top:7px;display:flex;align-items:center;gap:8px}

.hero{left:0;top:159px;width:1200px;height:506px;background:linear-gradient(90deg,#f2f2f2,#fafafa 60%,#f4f4f4)}
.hero-photo{left:60px;top:40px;width:560px;height:466px;border-radius:50% 50% 10% 10%;background:radial-gradient(ellipse at 50% 45%,#f0913a 0,#e0b24e 30%,#9cbc58 55%,#d2b48c 80%,#eee 100%)}
.hero h1{left:646px;top:140px;font-size:52px;font-weight:700;color:#111;letter-spacing:-.5px}
.hero h2{left:651px;top:208px;font-size:23px;font-weight:600;color:#111}
.search{left:652px;top:253px;width:486px;height:48px;border:2px solid var(--green);border-radius:3px;background:#fff;font-size:24px;font-weight:300;color:#aaa;padding:6px 24px}
.search svg{position:absolute;right:14px;top:11px}

.section-title{left:0;width:1200px;text-align:center;font-size:25px;font-weight:500;color:#111}
.section-lede{left:100px;width:1000px;text-align:center;font-size:15px;letter-spacing:3px;line-height:22px;color:#222}

.about-frame{left:127px;top:921px;width:338px;height:338px;background:var(--green)}
.about-photo{left:145px;top:937px;width:338px;height:337px;background:linear-gradient(160deg,#d9cfc4,#b85a4a 40%,#8fb25a 70%,#e4e4d4)}
.about-text{left:568px;top:916px;width:620px;font-size:15px;line-height:24.6px;letter-spacing:2.8px;color:#222;white-space:nowrap}
.btn{background:var(--green);color:#fff;text-align:center}
.btn-shop{left:959px;top:1233px;width:169px;height:41px;line-height:41px;font-size:15px;font-weight:600;letter-spacing:3px}

.benefits{left:0;top:1345px;width:1200px;height:940px;background:var(--soft)}
.grid{left:44px;top:1571px;width:1113px;height:625px;background:#fff;box-shadow:0 2px 6px rgba(0,0,0,.06)}
.photo-a{left:44px;top:1571px;width:556px;height:312px;background:linear-gradient(120deg,#6e8a5e,#c8563f 35%,#e3b44a 55%,#a9c7d8 80%,#567048)}
.photo-b{left:600px;top:1883px;width:557px;height:313px;background:linear-gradient(180deg,#d5d3cc 0,#bdb8ad 45%,#8c7a4a 60%,#5e5a30 100%)}
.panel h3{font-size:18px;font-weight:500;color:#222;margin-bottom:14px}
.panel li{list-style:none;font-size:18px;font-weight:300;color:#333;line-height:38px;white-space:nowrap}
.panel .btn{position:absolute;height:32px;line-height:32px;width:146px;font-size:14px}

.banner{left:0;top:2285px;width:1200px;height:303px;background:linear-gradient(180deg,#383a4a,#2f3142);color:#fff;text-align:center}
.banner h2{position:absolute;left:0;width:1200px;top:66px;font-size:24px;font-weight:600}
.banner p{position:absolute;left:0;width:1200px;top:110px;font-size:24px;font-weight:400}
.banner .btn{position:absolute;left:499px;top:191px;width:270px;height:46px;line-height:46px;font-size:26px}

.features{left:0;top:2588px;width:1200px;height:141px;background:var(--green);color:#fff}
.feature{top:52px;display:flex;gap:20px;align-items:center}
.feature b{display:block;font-size:17px;font-weight:500}
.feature small{display:block;font-size:15px;margin-top:4px}

.footer{left:0;top:2729px;width:1200px;height:245px;background:var(--dark);color:#fff}
.footer h4{font-size:20px;font-weight:600;margin-bottom:12px}
.footer .row{display:flex;gap:16px;align-items:center;font-size:16px;height:35px}
.footer .lnk{font-size:16px;line-height:34px}
.email{width:307px;height:36px;background:#fff;color:#aaa;font-size:15px;padding:7px 18px;position:relative;margin-top:14px}
.email svg{position:absolute;right:12px;top:9px}
.pay{top:200px;display:flex;gap:15px;align-items:flex-end}
.pay .label{font-size:11px;color:#fff;margin-right:-2px}
.card{width:59px;height:38px;background:#fff;border-radius:3px;border:2px solid #c9c9d2;display:flex;align-items:center;justify-content:center;font-size:10px;font-weight:600;color:#2e2f3e}
.copy{left:0;top:2974px;width:1200px;height:42px;background:var(--black);color:#fff;font-size:11px}
</style>
</head>
<body>

<div class="abs topbar">
  <span class="abs welcome">Welcome to Website &nbsp;Name..!</span>
  <span class="abs links">Join As A Seller &nbsp; | &nbsp; Log In To Account</span>
</div>

<header class="abs header">
  <span class="abs contact" style="left:42px">
    <svg width="14" height="14" viewBox="0 0 24 24" fill="#555"><path d="M6.6 10.8a15 15 0 006.6 6.6l2.2-2.2c.3-.3.7-.4 1-.2 1.1.4 2.3.6 3.6.6.6 0 1 .4 1 1V20c0 .6-.4 1-1 1A17 17 0 013 4c0-.6.4-1 1-1h3.5c.6 0 1 .4 1 1 0 1.3.2 2.5.6 3.6.1.3 0 .7-.2 1z"/></svg>
    +1 (555) 014-2290
  </span>
  <span class="abs contact" style="left:200px">
    <svg width="14" height="12" viewBox="0 0 24 18" fill="#555"><path d="M0 0h24v2L12 10 0 2zM0 4l12 8 12-8v14H0z"/></svg>
    <u>hello@brightacre.com</u>
  </span>
  <div class="abs logo">BRIGHTACRE</div>
  <span class="abs tool" style="left:893px">
    <svg width="14" height="14" viewBox="0 0 24 24"><circle cx="10" cy="10" r="7" fill="none" stroke="#555" stroke-width="3"/><path d="M15 15l7 7" stroke="#555" stroke-width="3"/></svg>Search
  </span>
  <span class="abs tool" style="left:1010px">
    <svg width="14" height="13" viewBox="0 0 24 22" fill="#555"><path d="M12 22L2 12A6 6 0 0112 4a6 6 0 0110 8z"/></svg>Wishlist
  </span>
  <span class="abs tool" style="left:1122px">
    <svg width="15" height="14" viewBox="0 0 24 22" fill="#555"><path d="M0 0h5l1 4h18l-3 10H8L4 2H0z"/><circle cx="9" cy="19" r="2"/><circle cx="19" cy="19" r="2"/></svg>10
  </span>
</header>

<nav class="abs nav">
  <span style="left:436px">Categories <svg width="10" height="6"><path d="M0 0h10L5 6z" fill="#fff"/></svg></span>
  <span style="left:567px">Current Offers</span>
  <span style="left:721px">Shops <svg width="10" height="6"><path d="M0 0h10L5 6z" fill="#fff"/></svg></span>
</nav>

<section class="abs hero">
  <div class="abs hero-photo" role="img" aria-label="Paper grocery bag spilling fresh vegetables and fruit"></div>
  <h1 class="abs">Direct From Farm..!</h1>
  <h2 class="abs">Find your products</h2>
  <div class="abs search">Type your products
    <svg width="24" height="24" viewBox="0 0 24 24"><circle cx="10" cy="10" r="7" fill="none" stroke="#bbb" stroke-width="2.5"/><path d="M15 15l7 7" stroke="#bbb" stroke-width="2.5"/></svg>
  </div>
</section>

<h2 class="abs section-title" style="top:747px">What Is This About</h2>
<p class="abs section-lede" style="top:798px">Lorem Ipsum is simply dummy text of the printing and typesetting industry.Lorem<br>is simply dummy &nbsp;text of the printing and typesetting industry.</p>

<div class="abs about-frame"></div>
<div class="abs about-photo" role="img" aria-label="Smiling shopper buying vegetables at a farmers market stall"></div>
<p class="abs about-text">Lorem Ipsum is simply dummy text of the printing<br>and typesetting industry. Lorem Ipsum has been the<br>industry's standard dummy text ever since the 1500s,<br>when an unknown printer took a galley of type and<br>scrambled it to make a type specimen book. It has<br>survived not only five centuries, but also the leap<br>into electronic typesetting, remaining essentially<br>unchanged. It was popularised in the 1960s with the<br>release of Letterline sheets containing Lorem Ipsum<br>passages, and more recently with desktop publish-<br>ing software like PageSetter including versions<br>of Lorem Ipsum.</p>
<a class="abs btn btn-shop">GO TO SHOP</a>

<section class="abs benefits"></section>
<h2 class="abs section-title" style="top:1390px">Customer &amp; Farmer Benefits</h2>
<p class="abs section-lede" style="top:1441px">Lorem Ipsum is simply dummy text of the printing and typesetting industry.Lorem<br>is simply dummy &nbsp;text of the printing and typesetting industry.</p>

<div class="abs grid"></div>
<div class="abs photo-a" role="img" aria-label="Farmer handing a crate of vegetables to a customer at a market"></div>
<div class="abs panel" style="left:622px;top:1596px;width:520px;height:280px">
  <h3>Benifits For Customer</h3>
  <ul>
    <li>1 . Lorem ipsum dolor sit amet, consectetur adipiscing elit.</li>
    <li>2 . Quisque at diam pharetra, dapibus mi ac, mollis eros.</li>
    <li>3 . Cras ornare risus et diam cursus interdum.</li>
    <li>4 . Praesent efficitur orci facilisis consequat tincidunt.</li>
    <li>5 . Lorem ipsum dolor sit amet, consectetur adipiscing elit.</li>
  </ul>
  <a class="btn" style="left:359px;top:237px">SEARCH NOW</a>
</div>
<div class="abs panel" style="left:60px;top:1907px;width:530px;height:280px">
  <h3>Benifits For Formes</h3>
  <ul>
    <li>1 . Lorem ipsum dolor sit amet, consectetur adipiscing elit.</li>
    <li>2 . Quisque at diam pharetra, dapibus mi ac, mollis eros.</li>
    <li>3 . Cras ornare risus et diam cursus interdum.</li>
    <li>4 . Praesent efficitur orci facilisis consequat tincidunt.</li>
    <li>5 . Lorem ipsum dolor sit amet, consectetur adipiscing elit.</li>
  </ul>
  <a class="btn" style="left:349px;top:238px">VIEW MORE</a>
</div>
<div class="abs photo-b" role="img" aria-label="Farmer driving an old tractor across a field at dusk"></div>

<section class="abs banner" role="img" aria-label="Dark overlay on a photo of fresh produce">
  <h2>WE HAVE MULTIPLE FORMS IN A SINGLE MARKETPLACE</h2>
  <p>Do You Want To Visit ?</p>
  <a class="btn">Visit Forms</a>
</section>

<section class="abs features">
  <div class="abs feature" style="left:50px">
    <svg width="44" height="36" viewBox="0 0 44 36" fill="#fff"><rect x="0" y="2" width="26" height="24" rx="2"/><path d="M28 10h8l8 9v9H28z"/><circle cx="10" cy="30" r="5" stroke="#7cbb10" stroke-width="2"/><circle cx="35" cy="30" r="5" stroke="#7cbb10" stroke-width="2"/></svg>
    <div><b>Free Delivery</b><small>Free Delivery over 250 $</small></div>
  </div>
  <div class="abs feature" style="left:464px">
    <svg width="38" height="34" viewBox="0 0 38 34"><path d="M4 22V18a15 15 0 0130 0v4" fill="none" stroke="#fff" stroke-width="4"/><rect x="2" y="20" width="9" height="14" rx="2" fill="#fff"/><rect x="27" y="20" width="9" height="14" rx="2" fill="#fff"/></svg>
    <div><b>24 / 7 Support</b><small>We support 24 / 7 everyday</small></div>
  </div>
  <div class="abs feature" style="left:857px">
    <svg width="34" height="32" viewBox="0 0 34 32" fill="#fff"><rect x="0" y="9" width="34" height="8"/><rect x="3" y="19" width="28" height="13"/><rect x="15" y="9" width="4" height="23" fill="#7cbb10"/><path d="M17 9C12 0 6 3 9 8zM17 9c5-9 11-6 8-1z"/></svg>
    <div><b>Min. 20% Offer</b><small>We provide minimum 30% Offer</small></div>
  </div>
</section>

<footer class="abs footer">
  <div class="abs" style="left:51px;top:30px">
    <h4>Contact Information</h4>
    <div class="row"><svg width="20" height="20" viewBox="0 0 24 24" fill="#fff"><path d="M6.6 10.8a15 15 0 006.6 6.6l2.2-2.2c.3-.3.7-.4 1-.2 1.1.4 2.3.6 3.6.6.6 0 1 .4 1 1V20c0 .6-.4 1-1 1A17 17 0 013 4c0-.6.4-1 1-1h3.5c.6 0 1 .4 1 1 0 1.3.2 2.5.6 3.6.1.3 0 .7-.2 1z"/></svg>+1 (555) 018-3341</div>
    <div class="row"><svg width="20" height="20" viewBox="0 0 24 24" fill="#fff"><path d="M12 0a8 8 0 018 8c0 6-8 16-8 16S4 14 4 8a8 8 0 018-8z"/></svg>14 Orchard Lane, Millbrook, 40211</div>
    <div class="row"><svg width="20" height="16" viewBox="0 0 24 18" fill="#fff"><path d="M0 0h24v2L12 10 0 2zM0 4l12 8 12-8v14H0z"/></svg>support@brightacre.com</div>
  </div>
  <div class="abs" style="left:507px;top:27px">
    <h4 style="margin-bottom:4px">Usefull Links</h4>
    <div class="lnk">Privacy Policy</div>
    <div class="lnk">Terms &amp; Condition</div>
    <div class="lnk">Login/Register As Seller</div>
  </div>
  <div class="abs" style="left:850px;top:27px">
    <h4 style="margin-bottom:12px">Usefull Links</h4>
    <div style="font-size:16px">Subscribe To Our Newsletter</div>
    <div class="email">Email
      <svg width="18" height="18" viewBox="0 0 24 24" fill="#999"><path d="M0 10L24 0 18 24l-6-8-4 5v-7z"/></svg>
    </div>
  </div>
  <div class="abs pay" style="left:735px">
    <span class="label">We Accept</span>
    <span class="card">Paylo</span>
    <span class="card">Cardo</span>
    <span class="card">Mintpay</span>
    <span class="card">Swiftcard</span>
    <span class="card">Walletly</span>
  </div>
</footer>

<div class="abs copy">
  <span class="abs" style="left:51px;top:14px">@ Copywrite to brightacre.com &amp; Group</span>
  <span class="abs" style="right:44px;top:14px">Help &nbsp;| &nbsp; Sitemap</span>
</div>

</body>
</html>
```